Design a Retail Box for Industrial Welding Helmets

We are excited to launch a design contest for our product's new retail packaging.
The products are 2 welding helmets.
Product 1 is Brontal helmet and product 2 is Veltrix helmet.
We are seeking for :
A) 1 main design of the box with minor adjustments for the 2 different models (Brontal and Veltrix)
B) 1 design for the sticker of Brontal (font)
C)1 design for the sticker of Veltrix (font)
Attached you will find:
1)Brand logo
2)Reference of welding wire packaging
3)Reference of welding torch packaging
4)Photo of Brontal model
5)Data of Brontal model to be included
6)Photo of Veltrix model
7)Data of Veltrix model to be included
8)Dieline Template of the box in .ai and .jpg
9)Vectors for the different uses of the helmets
Your design should reflect our brand and communicate the product's value while standing out on retail shelves.
The winner will be selected based on creativity, brand alignment, and overall design aesthetics.
We look forward to seeing your creative concepts.
Target Market(s)
Industrial and Retail
Industry/Entity Type
Welding, Retail, Hardware
Colors
Designer to choose colors to be used in the design.
Look and feel
Each slider illustrates characteristics of the customer's brand and the style your logo design should communicate.

```html
<!DOCTYPE html>
<html lang="en">
<head>
<meta charset="utf-8">
<title>Norvane Veltrix Welding Helmet – Retail Box Dieline</title>
<link rel="stylesheet" href="https://fonts.googleapis.com/css2?family=Montserrat:wght@300;400;500;700;800;900&display=swap">
<style>
  :root {
    --paper: #ffffff;
    --night: #0c0414;
    --deep: #1d0a33;
    --violet: #4a1f7a;
    --glow: #6b34b0;
    --band: #5a2a88;
    --ribbon: #5b2a93;
    --white: #ffffff;
    --muted: #d9d2e6;
    --cut: #ee2a2a;
    --fold: #1e9b2e;
    --helmet-dark: #17171b;
    --helmet-mid: #3b3b44;
  }
  * { box-sizing: border-box; margin: 0; padding: 0; }
  html, body { width: 1200px; height: 963px; overflow: hidden; background: var(--paper); }
  body { position: relative; font-family: "Montserrat", sans-serif; color: var(--white); }

  .dieline { position: absolute; left: 0; top: 0; width: 1200px; height: 963px; pointer-events: none; z-index: 3; }

  .panel {
    position: absolute; top: 441px; height: 354px; overflow: hidden;
    background:
      radial-gradient(ellipse 70% 45% at 55% 22%, rgba(107,52,176,.75), transparent 70%),
      radial-gradient(ellipse 60% 40% at 20% 45%, rgba(74,31,122,.6), transparent 70%),
      linear-gradient(180deg, var(--deep) 0%, var(--violet) 22%, #2a0f49 45%, var(--night) 100%);
  }
  .panel--front-a { left: 102px; width: 269px; }
  .panel--side-a  { left: 371px; width: 247px; }
  .panel--front-b { left: 618px; width: 270px; }
  .panel--side-b  { left: 888px; width: 246px; }

  .brand { position: absolute; top: 24px; width: 90px; display: flex; align-items: center; gap: 4px; justify-content: center; }
  .brand__dot { width: 9px; height: 9px; border-radius: 50%; background: var(--white); }
  .brand__name { font-weight: 700; font-size: 12px; letter-spacing: 1px; color: var(--white); }

  .ribbon {
    position: absolute; right: 3px; top: 1px; width: 128px; height: 19px;
    background: var(--ribbon); border-radius: 0 0 0 14px;
    text-align: center; font-weight: 900; font-size: 12px; line-height: 19px; letter-spacing: .2px;
  }
  .ribbon__sub { position: absolute; right: 20px; top: 22px; font-weight: 800; font-size: 7px; letter-spacing: .2px; }

  .features { position: absolute; left: 14px; top: 90px; list-style: none; }
  .feature { display: flex; align-items: center; gap: 5px; height: 25px; margin-bottom: 9.5px; }
  .feature__icon {
    width: 25px; height: 25px; border: 1.3px solid var(--white); border-radius: 5px;
    display: flex; align-items: center; justify-content: center; flex: none;
  }
  .feature__text { font-size: 6.2px; font-weight: 400; line-height: 1.15; color: var(--muted); }
  .swatch { width: 17px; height: 17px; border-radius: 50%;
    background: radial-gradient(circle, #fff 0 15%, transparent 60%), conic-gradient(#f33, #fc3, #6e3, #3cf, #36f, #c3f, #f33); }

  .helmet {
    position: absolute; left: 110px; top: 58px; width: 134px; height: 185px;
    border-radius: 48% 42% 38% 45% / 40% 36% 48% 50%;
    background: radial-gradient(ellipse at 35% 25%, var(--helmet-mid), var(--helmet-dark) 65%);
  }

  .title { position: absolute; left: 22px; top: 242px; }
  .title__brand { font-weight: 400; font-size: 21px; letter-spacing: 2px; line-height: 1; }
  .title__model { font-weight: 900; font-size: 43px; line-height: 1; letter-spacing: -.5px; margin-top: 0; }
  .title__kind { display: block; text-align: right; font-weight: 400; font-size: 15px; line-height: 1; letter-spacing: .3px;
    color: transparent; -webkit-text-stroke: .6px var(--white); margin-top: -1px; }

  .band { position: absolute; left: 0; right: 0; bottom: 0; height: 25px; background: var(--band);
    display: flex; align-items: center; justify-content: space-between; padding: 0 6px; }
  .band__tag { font-weight: 700; font-size: 10.5px; letter-spacing: .2px; }
  .processes { display: flex; gap: 5px; }
  .process { width: 17px; height: 16px; border: 1px solid var(--white); border-radius: 2px; background: #fff1;
    font-size: 3.5px; font-weight: 800; text-align: center; padding-top: 1px; }

  .lid {
    position: absolute; left: 102px; top: 195px; width: 269px; height: 246px; overflow: hidden;
    transform: rotate(180deg);
    background:
      radial-gradient(ellipse 60% 45% at 45% 60%, rgba(107,52,176,.7), transparent 70%),
      linear-gradient(0deg, var(--deep) 0%, var(--violet) 30%, #2a0f49 60%, var(--night) 100%);
  }
  .lid .brand { top: 38px; left: 86px; }
  .lid .helmet { left: 177px; top: 54px; width: 91px; height: 128px; }
  .lid .title { left: 10px; top: 88px; }
  .lid .title__brand { font-size: 14px; }
  .lid .title__model { font-size: 31px; }
  .lid .title__kind { font-size: 10px; }
  .lid-features { position: absolute; left: 8px; right: 8px; top: 216px; display: flex; justify-content: space-between; list-style: none; }
  .lid-features .feature { height: 19px; margin: 0; gap: 3px; }
  .lid-features .feature__icon { width: 18px; height: 18px; border-radius: 4px; }
  .lid-features .feature__text { font-size: 4.4px; }
  .lid-features .swatch { width: 13px; height: 13px; }

  .tuck-tab { position: absolute; left: 167px; top: 166px; width: 138px; height: 29px; background: var(--night);
    border-radius: 14px 14px 0 0; }
  .tuck-slot { position: absolute; left: 207px; top: 191px; width: 59px; height: 4px; background: var(--paper); border-radius: 2px; }
</style>
</head>
<body>

<div class="tuck-tab"></div>
<div class="tuck-slot"></div>

<section class="lid">
  <div class="brand"><span class="brand__dot"></span><span class="brand__name">NORVANE</span></div>
  <div class="helmet" role="img" aria-label="Product photo of the black auto-darkening welding helmet"></div>
  <div class="title">
    <p class="title__brand">NORVANE</p>
    <p class="title__model">VELTRIX</p>
    <span class="title__kind">WELDING HELMET</span>
  </div>
  <ul class="lid-features">
    <li class="feature"><span class="feature__icon"><svg width="12" height="12" viewBox="0 0 14 14" fill="none" stroke="#fff" stroke-width="1.6"><path d="M1 5V1h4M9 1h4v4M13 9v4H9M5 13H1V9M1 1l4 4M13 1L9 5M13 13L9 9M1 13l4-4"/></svg></span><span class="feature__text">Large Viewing Lens<br>3.94" x 3.15"</span></li>
    <li class="feature"><span class="feature__icon"><svg width="12" height="12" viewBox="0 0 14 14" fill="none" stroke="#fff" stroke-width="1.4"><circle cx="7" cy="7" r="5.5"/><path d="M7 3.5V7l2.5 1.5"/></svg></span><span class="feature__text">Auto-Darkening in<br>1/25000s</span></li>
    <li class="feature"><span class="feature__icon"><svg width="12" height="10" viewBox="0 0 14 10" fill="none" stroke="#fff" stroke-width="1.2"><rect x="1" y="1" width="12" height="8"/><path d="M11 3v2M10 4h2M3 6v2M2 7h2"/></svg></span><span class="feature__text">Optical Clarity<br>1/1/1/2</span></li>
    <li class="feature"><span class="feature__icon"><span class="swatch"></span></span><span class="feature__text">TRUE Color</span></li>
  </ul>
</section>

<section class="panel panel--front-a">
  <div class="brand" style="left:1px"><span class="brand__dot"></span><span class="brand__name">NORVANE</span></div>
  <div class="ribbon">LARGE VIEW</div>
  <div class="ribbon__sub">WEILDING HALMET</div>
  <ul class="features">
    <li class="feature"><span class="feature__icon"><svg width="16" height="16" viewBox="0 0 14 14" fill="none" stroke="#fff" stroke-width="1.6"><path d="M1 5V1h4M9 1h4v4M13 9v4H9M5 13H1V9M1 1l4 4M13 1L9 5M13 13L9 9M1 13l4-4"/></svg></span><span class="feature__text">Large Viewing Lens<br>3.94" x 3.15"</span></li>
    <li class="feature"><span class="feature__icon"><svg width="16" height="16" viewBox="0 0 14 14" fill="none" stroke="#fff" stroke-width="1.4"><circle cx="7" cy="7" r="5.5"/><path d="M7 3.5V7l2.5 1.5"/></svg></span><span class="feature__text">Auto-Darkening in<br>1/25000s</span></li>
    <li class="feature"><span class="feature__icon"><svg width="16" height="12" viewBox="0 0 14 10" fill="none" stroke="#fff" stroke-width="1.2"><rect x="1" y="1" width="12" height="8"/><path d="M11 3v2M10 4h2M3 6v2M2 7h2"/></svg></span><span class="feature__text">Optical Clarity<br>1/1/1/2</span></li>
    <li class="feature"><span class="feature__icon"><span class="swatch"></span></span><span class="feature__text">TRUE Color</span></li>
  </ul>
  <div class="helmet" role="img" aria-label="Product photo of the black auto-darkening welding helmet"></div>
  <div class="title">
    <p class="title__brand">NORVANE</p>
    <p class="title__model">VELTRIX</p>
    <span class="title__kind">WELDING HELMET</span>
  </div>
  <div class="band">
    <span class="band__tag">The choice of experts.</span>
    <div class="processes"><span class="process">MIG</span><span class="process">TIG</span><span class="process">STICK</span><span class="process">PLASMA</span><span class="process">GRIND</span></div>
  </div>
</section>

<section class="panel panel--side-a">
  <div class="brand" style="left:2px"><span class="brand__dot"></span><span class="brand__name">NORVANE</span></div>
  <div class="band"><span class="band__tag" style="padding-left:3px">The choice of experts.</span></div>
</section>

<section class="panel panel--front-b">
  <div class="brand" style="left:2px"><span class="brand__dot"></span><span class="brand__name">NORVANE</span></div>
  <div class="ribbon" style="width:100px;right:3px">LARGE VIEW</div>
  <div class="ribbon__sub" style="right:16px">WEILDING HALMET</div>
  <ul class="features">
    <li class="feature"><span class="feature__icon"><svg width="16" height="16" viewBox="0 0 14 14" fill="none" stroke="#fff" stroke-width="1.6"><path d="M1 5V1h4M9 1h4v4M13 9v4H9M5 13H1V9M1 1l4 4M13 1L9 5M13 13L9 9M1 13l4-4"/></svg></span><span class="feature__text">Large Viewing Lens<br>3.94" x 3.15"</span></li>
    <li class="feature"><span class="feature__icon"><svg width="16" height="16" viewBox="0 0 14 14" fill="none" stroke="#fff" stroke-width="1.4"><circle cx="7" cy="7" r="5.5"/><path d="M7 3.5V7l2.5 1.5"/></svg></span><span class="feature__text">Auto-Darkening in<br>1/25000s</span></li>
    <li class="feature"><span class="feature__icon"><svg width="16" height="12" viewBox="0 0 14 10" fill="none" stroke="#fff" stroke-width="1.2"><rect x="1" y="1" width="12" height="8"/><path d="M11 3v2M10 4h2M3 6v2M2 7h2"/></svg></span><span class="feature__text">Optical Clarity<br>1/1/1/2</span></li>
    <li class="feature"><span class="feature__icon"><span class="swatch"></span></span><span class="feature__text">TRUE Color</span></li>
  </ul>
  <div class="helmet" role="img" aria-label="Product photo of the black auto-darkening welding helmet"></div>
  <div class="title">
    <p class="title__brand">NORVANE</p>
    <p class="title__model">VELTRIX</p>
    <span class="title__kind">WELDING HELMET</span>
  </div>
  <div class="band">
    <span class="band__tag">The choice of experts.</span>
    <div class="processes"><span class="process">MIG</span><span class="process">TIG</span><span class="process">STICK</span><span class="process">PLASMA</span><span class="process">GRIND</span></div>
  </div>
</section>

<section class="panel panel--side-b">
  <div class="brand" style="left:2px"><span class="brand__dot"></span><span class="brand__name">NORVANE</span></div>
  <div class="band"><span class="band__tag" style="padding-left:4px">The choice of experts.</span></div>
</section>

<svg class="dieline" viewBox="0 0 1200 963" fill="none" stroke-width="0.7">
  <g class="dieline__cut" stroke="var(--cut)">
    <path d="M102 441V195H167V181Q167 166 182 166H290Q305 166 305 181V195H371V441"/>
    <path d="M102 446L74 452V784L102 790"/>
    <path d="M102 795L166 915V933Q166 943 176 943H297Q307 943 307 933V915L371 795"/>
    <path d="M373 795V899H490Q500 899 506 884L492 855L618 795"/>
    <path d="M620 795V943H670Q680 943 682 933V915H825V933Q827 943 837 943H886V795"/>
    <path d="M888 795L1014 855L1000 884Q1002 899 1014 899H1133L1134 795"/>
    <path d="M373 441L385 395Q388 384 400 384H592Q603 384 606 395L617 441"/>
    <path d="M620 441L632 395Q635 384 647 384H865Q876 384 879 395L887 441"/>
    <path d="M890 441L902 395Q905 384 917 384H1108Q1119 384 1122 395L1134 441"/>
    <path d="M724 466V420Q724 412 732 412H773Q781 412 781 420V466"/>
    <path d="M684 436H724M781 436H823"/>
  </g>
  <g class="dieline__fold" stroke="var(--fold)">
    <path d="M102 441H371M618 441H888M102 441V795M371 441V795M618 441V795M888 441V795M724 466H781"/>
  </g>
</svg>

</body>
</html>
```